brolvix new business card design project

we need a new business card design. you can view info about us @ brolvix.example. i have attached an example of our previous card with our previous name that we no longer use. We really liked the design, colors etc. look below to see more info about this project. it asks for a limited number of words. please see our website for more info about our compnay.

Target Market(s)

law enforcement

Contact Information for Business Card

i have uploaded an example of what we used before that we liked.

Font styles to use
Serif

```html
<!DOCTYPE html>
<html lang="en">
<head>
<meta charset="utf-8">
<title>Brolvix business card</title>
<link rel="stylesheet" href="https://fonts.googleapis.com/css2?family=Roboto:wght@300;400;500&display=swap">
<style>
  :root {
    --backdrop: #d2d5d5;
    --card: #f4f4f3;
    --ink: #111111;
    --purple: #6a2c8e;
    --blue: #0f6fb0;
    --band: #0d4fa3;
    --band-light: #ffffff;
    --shadow: rgba(0, 0, 0, 0.18);
  }
  * { box-sizing: border-box; margin: 0; padding: 0; }
  html, body {
    width: 1200px;
    height: 889px;
    overflow: hidden;
    background: var(--backdrop);
    font-family: "Roboto", Arial, sans-serif;
    color: var(--ink);
  }
  .stage {
    position: relative;
    width: 1200px;
    height: 889px;
  }
  .card {
    position: absolute;
    top: 300px;
    width: 500px;
    height: 286px;
    background: var(--card);
    box-shadow: 0 10px 28px var(--shadow);
    overflow: hidden;
  }
  .card--front { left: 70px; }
  .card--back { left: 630px; }

  /* Front */
  .front-wordmark {
    position: absolute;
    left: 44px;
    top: 118px;
    font-size: 34px;
    font-weight: 300;
    letter-spacing: 6px;
  }
  .front-divider {
    position: absolute;
    left: 236px;
    top: 66px;
    width: 2px;
    height: 150px;
    background: var(--ink);
  }
  .contact {
    position: absolute;
    left: 262px;
    top: 78px;
  }
  .contact__name {
    font-size: 24px;
    font-weight: 500;
    margin-bottom: 14px;
  }
  .contact__first { color: var(--purple); }
  .contact__last { color: var(--blue); }
  .contact__line {
    font-size: 13px;
    line-height: 18px;
    font-weight: 400;
  }

  /* Back */
  .back-wordmark {
    position: absolute;
    left: 0;
    right: 0;
    top: 102px;
    text-align: center;
    font-size: 46px;
    font-weight: 300;
    letter-spacing: 9px;
  }
  .back-band {
    position: absolute;
    left: 0;
    bottom: 0;
    width: 500px;
    height: 40px;
  }
  .back-band__url {
    position: absolute;
    right: 28px;
    bottom: 8px;
    color: var(--band-light);
    font-size: 20px;
    font-weight: 500;
    letter-spacing: 0.5px;
  }
</style>
</head>
<body>
<main class="stage">
  <section class="card card--front" aria-label="Business card front">
    <div class="front-wordmark">BROLVIX</div>
    <div class="front-divider"></div>
    <div class="contact">
      <p class="contact__name"><span class="contact__first">Dana</span> <span class="contact__last">Mercer</span></p>
      <p class="contact__line">555.014.2290</p>
      <p class="contact__line">info@brolvix.example</p>
      <p class="contact__line">4120 Larkfield Road</p>
      <p class="contact__line">Fairview, TX 75000</p>
    </div>
  </section>

  <section class="card card--back" aria-label="Business card back">
    <div class="back-wordmark">BROLVIX</div>
    <svg class="back-band" viewBox="0 0 500 40" aria-hidden="true">
      <rect x="0" y="0" width="500" height="40" fill="var(--band)"/>
      <path d="M0 0 Q120 4 200 0 L200 6 Q110 12 0 8 Z" fill="var(--purple)"/>
    </svg>
    <div class="back-band__url">www.brolvix.example</div>
  </section>
</main>
</body>
</html>
```